QBrook718 Business Card Design

I am in need of a business card design.

Business Name: Harbor Stone 718 or Qbrook718 (we can try the business card with both variations)

I would like it to be somewhat different from the "average" business card

What do we do?

We link up with distributors of different items and we Market their products, sell their products, fulfill the shipment, and handle all customer service that goes along with it.

I will be uploading our logo as well as other business card ideas that i have seen and liked on the web.

I like the style of the "graphic design" business card that i uploaded. I was thinking maybe something like that but instead would read.

SYNC | SELL | SHIP

With maybe:
a computer or a Sync icon underneath SYNC
Some form of money sign underneath Sell
a delivery truck or something underneath SHIP.

And then I was thinking maybe put the logo on the back side like in the other business card that i uploaded.

I definitely want a double sided business card.

These are only my suggestions and if i was very confident in my idea then I wouldn't have to be on here. (So make what you think is nice because my opinion is probably not so great anyway!!)

Everything can be changed.

ALSO, For the logo
We can try and remove the text multi channel selling

For the Business card contact info:
Tom Haskins
CEO
2419 Pelkey Avenue
J7R-2B8
Montreal, Quebec

Thanks

Target Market(s)

Businesses

Industry/Entity Type

Information Technology

Font styles to use
Serif
Sans Serif
Decorative

Colors
34a6d6
33b8a4
aaaaaa
85cae6
33a6d7
0492cd
9d9d9d

Requirements
Must have
• Double Sided Business card
Nice to have
• Illustration graphics / Icons underneath the main points

```html
<!DOCTYPE html>
<html lang="en">
<head>
<meta charset="utf-8">
<title>Qbrook718 Business Card</title>
<link rel="stylesheet" href="https://fonts.googleapis.com/css2?family=Open+Sans:ital,wght@0,300;0,400;0,700;1,600;1,700&display=swap">
<style>
  :root {
    --backdrop: #a6b5b5;
    --card: #ffffff;
    --ink: #0a0b0c;
    --slate: #6d6e70;
    --icon: #58595b;
    --aqua: #00f6f8;
    --white: #ffffff;
  }
  * { margin: 0; padding: 0; box-sizing: border-box; }
  html, body {
    width: 1200px; height: 1200px; overflow: hidden;
    background: var(--backdrop);
    font-family: "Open Sans", Arial, sans-serif;
  }
  .card {
    position: absolute; left: 166px; width: 868px; height: 510px;
    background: var(--card); border-radius: 32px; overflow: hidden;
    box-shadow: 4px 6px 10px rgba(0,0,0,0.3);
  }
  .card--front { top: 59px; }
  .card--back { top: 631px; }

  .brand-name {
    position: absolute; font-weight: 700; font-size: 50px;
    letter-spacing: -1px; line-height: 1; white-space: nowrap;
  }
  .card--front .brand-name { left: 95px; top: 244px; color: var(--ink); }
  .card--back .brand-name { left: 112px; top: 172px; color: var(--aqua); }
  .brand-dot {
    position: absolute; width: 16px; height: 16px; border-radius: 50%;
  }
  .card--front .brand-dot { left: 368px; top: 224px; background: var(--ink); }
  .card--back .brand-dot { left: 385px; top: 152px; background: var(--aqua); }

  .name-panel {
    position: absolute; left: 468px; top: 0; width: 352px; height: 100%;
    background: var(--ink);
  }
  .rule { position: absolute; height: 3px; }
  .rule--grey { left: 95px; top: 314px; width: 373px; background: var(--slate); }
  .rule--white { left: 468px; top: 314px; width: 226px; background: var(--white); }
  .person-name {
    position: absolute; right: 116px; top: 243px;
    font-style: italic; font-weight: 700; font-size: 41px; letter-spacing: -0.5px;
    color: var(--white); white-space: nowrap;
  }
  .person-title {
    position: absolute; right: 116px; top: 295px;
    font-style: italic; font-weight: 600; font-size: 21px; color: var(--white);
  }

  .pillars {
    position: absolute; left: 420px; top: 162px;
    font-weight: 300; font-size: 30px; color: var(--slate);
    white-space: nowrap;
  }
  .pillars .sep { margin: 0 20px; }
  .rule--pillars { left: 386px; top: 211px; width: 482px; background: var(--slate); }
  .pillar-icon { position: absolute; top: 226px; width: 52px; height: 52px; }
  .pillar-icon--sync { left: 433px; }
  .pillar-icon--sell { left: 546px; }
  .pillar-icon--ship { left: 658px; }

  .company-band {
    position: absolute; left: 0; top: 385px; width: 100%; height: 62px;
    background: var(--aqua);
  }
  .company-name {
    position: absolute; left: 114px; top: -6px;
    font-style: italic; font-weight: 700; font-size: 50px; letter-spacing: -1px;
    color: var(--white); white-space: nowrap;
  }
  .address-band {
    position: absolute; left: 0; top: 447px; width: 100%; height: 63px;
    background: var(--ink);
  }
  .address {
    position: absolute; left: 113px; top: 4px;
    font-size: 22px; color: var(--white); white-space: nowrap;
  }
</style>
</head>
<body>
  <section class="card card--front">
    <div class="name-panel"></div>
    <span class="brand-dot"></span>
    <div class="brand-name">Qbrook718</div>
    <div class="rule rule--grey"></div>
    <div class="rule rule--white"></div>
    <div class="person-name">Tom Haskins</div>
    <div class="person-title">CEO</div>
  </section>

  <section class="card card--back">
    <span class="brand-dot"></span>
    <div class="brand-name">Qbrook718</div>
    <div class="pillars">SYNC<span class="sep">|</span>SELL<span class="sep">|</span>SHIP</div>
    <div class="rule rule--pillars"></div>

    <svg class="pillar-icon pillar-icon--sync" viewBox="0 0 52 52" aria-label="Sync">
      <circle cx="26" cy="26" r="26" fill="var(--icon)"/>
      <path d="M14 24a12 12 0 0 1 21-7" fill="none" stroke="#fff" stroke-width="4"/>
      <path d="M38 11v10h-10z" fill="#fff"/>
      <path d="M38 28a12 12 0 0 1-21 7" fill="none" stroke="#fff" stroke-width="4"/>
      <path d="M14 41v-10h10z" fill="#fff"/>
    </svg>
    <svg class="pillar-icon pillar-icon--sell" viewBox="0 0 52 52" aria-label="Sell">
      <circle cx="26" cy="26" r="26" fill="var(--icon)"/>
      <text x="26" y="38" text-anchor="middle" font-family="Open Sans, sans-serif" font-weight="700" font-size="34" fill="#fff">$</text>
    </svg>
    <svg class="pillar-icon pillar-icon--ship" viewBox="0 0 52 52" aria-label="Ship">
      <circle cx="26" cy="26" r="26" fill="var(--icon)"/>
      <path d="M14 17h20l6 6v11H14z" fill="#fff"/>
      <rect x="7" y="19" width="6" height="2" fill="#fff"/>
      <rect x="5" y="24" width="8" height="2" fill="#fff"/>
      <rect x="7" y="29" width="6" height="2" fill="#fff"/>
      <circle cx="20" cy="35" r="3.5" fill="var(--icon)" stroke="#fff" stroke-width="2"/>
      <circle cx="34" cy="35" r="3.5" fill="var(--icon)" stroke="#fff" stroke-width="2"/>
    </svg>

    <div class="company-band">
      <div class="company-name">Harbor Stone 718</div>
    </div>
    <div class="address-band">
      <div class="address">2419 Pelkey Avenue, J7R-2B8, Montreal, Quebec</div>
    </div>
  </section>
</body>
</html>
```